Storytelling podcast needs podcast artwork

We need a logo design for a new podcast called 'Across Still Waters, Walking Home Again'. The podcast will tell the story of family whose young daughter suddenly and expectedly goes blind. We would like to see designs that play on the concepts of shading, transition, and contrast. The final design communicate the challenges of being in darkness and the reward of finding light.

Requirements
Must have
• 1800 x 1800 pixel image. No text in bottom 1/4 of image.

```html
<!DOCTYPE html>
<html lang="en">
<head>
<meta charset="utf-8">
<title>Across Still Waters, Walking Home Again — Podcast Artwork</title>
<link rel="stylesheet" href="https://fonts.googleapis.com/css2?family=Bebas+Neue&family=Oswald:wght@200&display=swap">
<style>
  :root {
    --page-white: #ffffff;
    --night: #050505;
    --frame-line: #2a2a2a;
    --title-dark: #231816;
    --title-light: #fff8dc;
    --glow-core: #ffffff;
    --glow-green: #5f7a3a;
    --path-ember: #3a1a0c;
  }
  html, body {
    margin: 0;
    padding: 0;
    width: 1196px;
    height: 1200px;
    overflow: hidden;
    background: var(--page-white);
  }
  .canvas {
    position: relative;
    width: 1196px;
    height: 1200px;
    background: var(--page-white);
  }
  .cover {
    position: absolute;
    left: 148px;
    top: 150px;
    width: 903px;
    height: 903px;
    box-sizing: border-box;
    border: 2px solid var(--frame-line);
    background: var(--night);
    overflow: hidden;
  }
  .cover-scene {
    position: absolute;
    inset: 0;
    background:
      radial-gradient(circle at 54% 57%, var(--glow-core) 0, var(--glow-core) 4%, rgba(200,220,180,0.85) 7%, rgba(95,122,58,0.75) 14%, rgba(30,40,20,0.6) 24%, transparent 34%),
      radial-gradient(ellipse 62% 48% at 54% 58%, rgba(58,26,12,0.55) 0, rgba(58,26,12,0.35) 60%, transparent 100%),
      var(--night);
  }
  .title {
    position: absolute;
    left: 67px;
    margin: 0;
    line-height: 1;
    white-space: nowrap;
  }
  .title-dark {
    font-family: "Bebas Neue", "Oswald", sans-serif;
    font-weight: 400;
    font-size: 120px;
    color: var(--title-dark);
  }
  .title-line-1 { top: 60px; }
  .title-line-2 { top: 196px; }
  .title-light {
    top: 326px;
    font-family: "Oswald", sans-serif;
    font-weight: 200;
    font-size: 160px;
    letter-spacing: -2px;
    color: var(--title-light);
  }
</style>
</head>
<body>
  <div class="canvas">
    <section class="cover">
      <div class="cover-scene" role="img" aria-label="Night view of a circular hedge labyrinth with a bright glowing light at its centre and a girl seen from behind looking towards it"></div>
      <h1 class="sr-title" style="position:absolute;width:1px;height:1px;overflow:hidden;clip:rect(0 0 0 0);margin:0;">Across Still Waters, Walking Home Again</h1>
      <p class="title title-dark title-line-1" aria-hidden="true">ACROSS STILL WATERS,</p>
      <p class="title title-dark title-line-2" aria-hidden="true">WALKING HOME</p>
      <p class="title title-light" aria-hidden="true">AGAIN</p>
    </section>
  </div>
</body>
</html>
```